KV MOTORS BANNER/SIGN DESIGN

Design a banner sign for outdoor use for KV MOTORS - a premium pre owned vehicle sales center. The size must be 36 feet in width
and 3 feet in height.

Information required: logo (attached)
-PREMIUM PRE-OWEND VEHICLE SALES
- 403.555.0172

perhaps in smaller font: BUY-SELL-TRADE

prefer white background but could possibly do red matching the logo

```html
<!DOCTYPE html>
<html lang="en">
<head>
<meta charset="utf-8">
<title>KV Motors Banner Sign</title>
<link href="https://fonts.googleapis.com/css2?family=Archivo+Black&family=Oswald:wght@500;600&display=swap" rel="stylesheet">
<style>
  :root {
    --brand-red: #dc2228;
    --ink: #0b0c0b;
    --paper: #ffffff;
    --stage-dark: #0b0c0b;
  }
  * { margin: 0; padding: 0; box-sizing: border-box; }
  html, body { width: 1200px; height: 667px; overflow: hidden; }
  body { position: relative; background: var(--paper); }
  .stage-light { position: absolute; left: 0; top: 0; width: 1200px; height: 359px; background: var(--paper); }
  .stage-dark { position: absolute; left: 0; top: 359px; width: 1200px; height: 308px; background: var(--stage-dark); }
  .banner { position: absolute; width: 693px; height: 59px; display: block; }
  .banner--on-light { left: 244px; top: 151px; }
  .banner--on-dark { left: 256px; top: 108px; }
  .banner__field { fill: var(--paper); }
  .banner--on-light .banner__field { stroke: var(--ink); stroke-width: 1.6; }
  .banner__divider { stroke: var(--ink); stroke-width: 1.2; }
  .brand-dot { fill: var(--brand-red); }
  .brand-name { font-family: "Archivo Black", sans-serif; font-size: 30px; fill: var(--ink); }
  .tagline { font-family: "Oswald", sans-serif; font-weight: 600; font-size: 17px; fill: var(--brand-red); }
  .services { font-family: "Archivo Black", sans-serif; font-size: 32px; fill: var(--ink); }
  .services__accent { fill: var(--brand-red); }
  .phone { font-family: "Archivo Black", sans-serif; font-size: 22px; fill: var(--brand-red); }
</style>
</head>
<body>
  <section class="stage-light">
    <svg class="banner banner--on-light" viewBox="0 0 693 59" aria-label="KV Motors banner, white version">
      <rect class="banner__field" x="0.8" y="0.8" width="691.4" height="57.4"/>
      <line class="banner__divider" x1="285" y1="2" x2="285" y2="58"/>
      <circle class="brand-dot" cx="48" cy="23" r="14"/>
      <text class="brand-name" x="72" y="35" textLength="194" lengthAdjust="spacingAndGlyphs">KV MOTORS</text>
      <text class="tagline" x="33" y="54" textLength="234" lengthAdjust="spacingAndGlyphs">PREMIUM PRE-OWEND VEHICLE SALES</text>
      <text class="services" x="302" y="32" textLength="372" lengthAdjust="spacingAndGlyphs">BUY-<tspan class="services__accent">SELL</tspan>-TRADE</text>
      <text class="phone" x="302" y="52" textLength="374" lengthAdjust="spacingAndGlyphs">403.555.0172</text>
    </svg>
  </section>
  <section class="stage-dark">
    <svg class="banner banner--on-dark" viewBox="0 0 693 59" aria-label="KV Motors banner on dark background">
      <rect class="banner__field" x="0" y="0" width="693" height="59"/>
      <line class="banner__divider" x1="285" y1="2" x2="285" y2="58"/>
      <circle class="brand-dot" cx="48" cy="23" r="14"/>
      <text class="brand-name" x="72" y="35" textLength="194" lengthAdjust="spacingAndGlyphs">KV MOTORS</text>
      <text class="tagline" x="33" y="54" textLength="234" lengthAdjust="spacingAndGlyphs">PREMIUM PRE-OWEND VEHICLE SALES</text>
      <text class="services" x="302" y="32" textLength="372" lengthAdjust="spacingAndGlyphs">BUY-<tspan class="services__accent">SELL</tspan>-TRADE</text>
      <text class="phone" x="302" y="52" textLength="374" lengthAdjust="spacingAndGlyphs">403.555.0172</text>
    </svg>
  </section>
</body>
</html>
```